Hooded Rogue - Game Company Site

Looking for a simple and sleek 3 page design for a game company site. Will provide a logo to be included in the design. Even though we specialize in flash games at the moment, we plan on expanding to other platforms and would like a site similar to console developer sites than flash game portals. Example: http://brightfoxle.com

Required Pages:
1. Home: advertising the latest game, big image, and possibly a news post
2. Games: a portfolio of games, each game will have a large image preview and some text, with a link to the game
3. About Us:
A roster of employees, each will have a picture and bio with name, alias, location, and some text.

Would be nice to have a theme inspired by "villains." The logo should provide the general feel we are looking for. You will find the logo attached as a .PSD (Photoshop) and a .PNG to give a quick preview. Vector .ai and .eps logos have also been attached. Feel free to split the text from the character or make any changes you feel necessary!

About Hooded Rogue
We create flash games and are hoping to expand to iPhone games and other platforms in the future!
Our latest game: http://www.playvantix.com/games/quirkloft/toadkin-quest-2-chapter-1

Target Market(s)

18-30 year old male tech and video game enthusiasts

Industry/Entity Type

Advertising

Requirements
Must have
• Must have the logo that is attached.

```html
<!DOCTYPE html>
<html lang="en">
<head>
<meta charset="utf-8">
<title>Hooded Rogue – About Us</title>
<link rel="stylesheet" href="https://fonts.googleapis.com/css2?family=Arimo:wght@400;700&family=Questrial&family=Luckiest+Guy&display=swap">
<style>
  :root {
    --bg-deep: #4a2f78;
    --bg-light: #7d5db4;
    --panel: #000000;
    --orange: #ff9c1f;
    --orange-dim: #b8701c;
    --gold: #ffc61a;
    --nav-purple: #7a55c8;
    --nav-text: #3a2466;
    --footer-text: #1c1230;
    --white: #ffffff;
  }
  * { box-sizing: border-box; margin: 0; padding: 0; }
  html, body { width: 1200px; height: 923px; overflow: hidden; }
  body {
    position: relative;
    font-family: "Arimo", Arial, sans-serif;
    background: radial-gradient(ellipse 900px 700px at 600px 923px, var(--bg-light), var(--bg-deep) 100%);
  }
  .brand {
    position: absolute; left: 185px; top: 60px;
    display: flex; align-items: center; gap: 10px;
  }
  .brand-mark { width: 34px; height: 34px; border-radius: 50%; background: var(--gold); }
  .brand-name {
    font-family: "Luckiest Guy", "Arial Black", sans-serif;
    font-size: 28px; color: var(--gold); letter-spacing: 0.5px;
  }
  .follow-top {
    position: absolute; left: 819px; top: 0; width: 224px; height: 53px;
    background: #0a0a0a; border-radius: 0 0 3px 3px;
    display: flex; align-items: center; gap: 10px; padding-left: 14px;
  }
  .follow-label {
    font-family: "Luckiest Guy", "Arial Black", sans-serif;
    font-size: 17px; color: var(--gold); padding-top: 3px;
  }
  .social-name { font-family: "Arimo", Arial, sans-serif; font-weight: 700; font-size: 11px; color: var(--white); }
  .main-nav { position: absolute; top: 99px; left: 642px; display: flex; gap: 16px; }
  .nav-item {
    height: 41px; display: flex; align-items: center; justify-content: center;
    font-family: "Luckiest Guy", "Arial Black", sans-serif; font-size: 18px;
    color: var(--nav-text); background: linear-gradient(var(--nav-purple), #6444b0);
    border: 1px solid #5a3d9a; border-radius: 2px; text-decoration: none; padding-top: 3px;
  }
  .nav-item.home { width: 106px; }
  .nav-item.games { width: 117px; }
  .nav-item.about { width: 148px; background: #0a0a0a; color: var(--gold); border-color: #222; }
  .roster {
    position: absolute; left: 153px; top: 161px; width: 899px; height: 662px;
    background: var(--panel); border-radius: 6px;
    padding: 32px 0 0 34px;
    display: grid; grid-template-columns: 442px 442px; grid-auto-rows: 210px;
  }
  .member { position: relative; }
  .member-photo {
    position: absolute; left: 0; top: 0; width: 136px; height: 120px;
    background: linear-gradient(135deg, #6b5a4c, #b9a899 55%, #4b4540);
  }
  .member-info { position: absolute; left: 154px; top: -4px; }
  .member-name { font-family: "Questrial", Arial, sans-serif; font-size: 27px; color: var(--orange); line-height: 32px; }
  .member-label { font-size: 12.5px; color: var(--orange-dim); line-height: 15px; }
  .member-value { font-size: 15.5px; color: var(--orange); line-height: 18px; display: flex; align-items: center; gap: 12px; }
  .flag { display: inline-flex; width: 24px; height: 16px; }
  .flag span { flex: 1; }
  .member-bio {
    position: absolute; left: 3px; top: 144px; width: 385px;
    font-size: 12px; font-weight: 700; color: var(--orange); line-height: 17px;
  }
  .site-footer { position: absolute; left: 156px; top: 849px; }
  .footer-nav { display: flex; gap: 25px; }
  .footer-nav a { font-size: 14.5px; font-weight: 700; color: var(--footer-text); text-decoration: none; }
  .footer-nav a + a { margin-left: -7px; }
  .footer-contact { margin-top: 4px; font-size: 12.5px; color: var(--footer-text); }
  .follow-bottom { position: absolute; left: 874px; top: 860px; display: flex; align-items: center; gap: 10px; }
  .follow-bottom .follow-label { color: var(--footer-text); }
  .follow-bottom .social-name { color: var(--footer-text); }
</style>
</head>
<body>
  <header>
    <div class="brand">
      <span class="brand-mark"></span>
      <span class="brand-name">Hooded Rogue</span>
    </div>
    <div class="follow-top">
      <span class="follow-label">Follow us:</span>
      <span class="social-name">Pagefold</span>
      <span class="social-name">Chirpnest</span>
    </div>
    <nav class="main-nav">
      <a class="nav-item home" href="#">Home</a>
      <a class="nav-item games" href="#">Games</a>
      <a class="nav-item about" href="#">About Us</a>
    </nav>
  </header>

  <main class="roster">
    <article class="member">
      <div class="member-photo" role="img" aria-label="Portrait photo of Ivo Marlen"></div>
      <div class="member-info">
        <h2 class="member-name">Ivo Marlen</h2>
        <div class="member-label">Alias:</div><div class="member-value">Biggles</div>
        <div class="member-label">Role:</div><div class="member-value">Designer</div>
        <div class="member-label">Location:</div>
        <div class="member-value">Belgium <span class="flag"><span style="background:#111"></span><span style="background:#f5d11a"></span><span style="background:#e0222b"></span></span></div>
      </div>
      <p class="member-bio">Lorem ipsum dolor sit amet, consectetur adipisicing elit, sed do eiusmod tempor incididunt ut labore et dolore magna aliqua. Ut enim ad minim veniam,</p>
    </article>
    <article class="member">
      <div class="member-photo" role="img" aria-label="Portrait photo of Tobin Ashgrove"></div>
      <div class="member-info">
        <h2 class="member-name">Tobin Ashgrove</h2>
        <div class="member-label">Alias:</div><div class="member-value">Biggles</div>
        <div class="member-label">Role:</div><div class="member-value">Designer</div>
        <div class="member-label">Location:</div>
        <div class="member-value">Belgium <span class="flag"><span style="background:#111"></span><span style="background:#f5d11a"></span><span style="background:#e0222b"></span></span></div>
      </div>
      <p class="member-bio">Lorem ipsum dolor sit amet, consectetur adipisicing elit, sed do eiusmod tempor incididunt ut labore et dolore magna aliqua. Ut enim ad minim veniam,</p>
    </article>
    <article class="member">
      <div class="member-photo" role="img" aria-label="Portrait photo of Rafe Dunmore"></div>
      <div class="member-info">
        <h2 class="member-name">Rafe Dunmore</h2>
        <div class="member-label">Alias:</div><div class="member-value">Biggles</div>
        <div class="member-label">Role:</div><div class="member-value">Designer</div>
        <div class="member-label">Location:</div>
        <div class="member-value">Belgium <span class="flag"><span style="background:#111"></span><span style="background:#f5d11a"></span><span style="background:#e0222b"></span></span></div>
      </div>
      <p class="member-bio">Lorem ipsum dolor sit amet, consectetur adipisicing elit, sed do eiusmod tempor incididunt ut labore et dolore magna aliqua. Ut enim ad minim veniam,</p>
    </article>
    <article class="member">
      <div class="member-photo" role="img" aria-label="Portrait photo of Silas Verhoek"></div>
      <div class="member-info">
        <h2 class="member-name">Silas Verhoek</h2>
        <div class="member-label">Alias:</div><div class="member-value">Biggles</div>
        <div class="member-label">Role:</div><div class="member-value">Designer</div>
        <div class="member-label">Location:</div>
        <div class="member-value">Belgium <span class="flag"><span style="background:#111"></span><span style="background:#f5d11a"></span><span style="background:#e0222b"></span></span></div>
      </div>
      <p class="member-bio">Lorem ipsum dolor sit amet, consectetur adipisicing elit, sed do eiusmod tempor incididunt ut labore et dolore magna aliqua. Ut enim ad minim veniam,</p>
    </article>
    <article class="member">
      <div class="member-photo" role="img" aria-label="Portrait photo of Milo Brankett"></div>
      <div class="member-info">
        <h2 class="member-name">Milo Brankett</h2>
        <div class="member-label">Alias:</div><div class="member-value">Biggles</div>
        <div class="member-label">Role:</div><div class="member-value">Designer</div>
        <div class="member-label">Location:</div>
        <div class="member-value">Belgium <span class="flag"><span style="background:#111"></span><span style="background:#f5d11a"></span><span style="background:#e0222b"></span></span></div>
      </div>
      <p class="member-bio">Lorem ipsum dolor sit amet, consectetur adipisicing elit, sed do eiusmod tempor incididunt ut labore et dolore magna aliqua. Ut enim ad minim veniam,</p>
    </article>
    <article class="member">
      <div class="member-photo" role="img" aria-label="Portrait photo of Otis Calloway"></div>
      <div class="member-info">
        <h2 class="member-name">Otis Calloway</h2>
        <div class="member-label">Alias:</div><div class="member-value">Biggles</div>
        <div class="member-label">Role:</div><div class="member-value">Designer</div>
        <div class="member-label">Location:</div>
        <div class="member-value">Belgium <span class="flag"><span style="background:#111"></span><span style="background:#f5d11a"></span><span style="background:#e0222b"></span></span></div>
      </div>
      <p class="member-bio">Lorem ipsum dolor sit amet, consectetur adipisicing elit, sed do eiusmod tempor incididunt ut labore et dolore magna aliqua. Ut enim ad minim veniam,</p>
    </article>
  </main>

  <footer class="site-footer">
    <nav class="footer-nav">
      <a href="#">HOME</a>
      <a href="#">GAMES</a>
      <a href="#">ABOUT US</a>
    </nav>
    <p class="footer-contact">info@roguecrafthq.com &nbsp;|&nbsp; Call: 555-210-4187| &nbsp;Fax: 555-210-4187 &nbsp;| © All Rights Reserved</p>
  </footer>
  <div class="follow-bottom">
    <span class="follow-label">Follow us:</span>
    <span class="social-name">Pagefold</span>
    <span class="social-name">Chirpnest</span>
  </div>
</body>
</html>
```